Flyers

Please refer to the attachment. I have been using this design for quite some time now and looks like the design is not attracting anymore attention.
Would prefer similar/new wording with new design that would work.
Remember these flyers get distributed to letter boxes and usually with lots of other letters, newspapers and etc so if the color or design is not appealing chances are that the flyers might not even be seen.
Recommendation: May be NZ $100 note pics in the back ground would help. A nice picture of Vorano van, Ridgewalker 4wd and Truck would preferred.

With the wordings I would like to may be alter or may be even add some more that we buy only Vans, 4WDs, SUV, Trucks. And we can come to you anywhere.

PLEASE DELETE "we sell car parts"
Good luck.

Note: Phone no needs to be changed to 0800394826 and replace address with NATION WIDE but leave website and email on.

```html
<!DOCTYPE html>
<html lang="en">
<head>
<meta charset="utf-8">
<title>Keystone Vehicle Removal – Flyer</title>
<link rel="stylesheet" href="https://fonts.googleapis.com/css2?family=Archivo+Black&family=Oswald:wght@400;500&family=Archivo:ital,wght@1,800&display=swap">
<style>
  :root {
    --red: #e01b24;
    --black: #0b0b0b;
    --charcoal: #1c1c1c;
    --silver-light: #f2f2f2;
    --silver-mid: #c9c9c9;
    --white: #ffffff;
  }
  * { box-sizing: border-box; margin: 0; padding: 0; }
  html, body { width: 907px; height: 1200px; overflow: hidden; background: var(--black); }
  .flyer {
    position: relative; width: 907px; height: 1200px; overflow: hidden;
    background: linear-gradient(180deg, var(--charcoal) 0%, var(--black) 100%);
    font-family: "Archivo Black", "Arial Black", sans-serif;
  }
  .silver-field {
    position: absolute; left: 0; top: 0; width: 907px; height: 690px;
    background: radial-gradient(ellipse at 50% 35%, var(--silver-light) 0%, #dedede 45%, var(--silver-mid) 100%);
  }
  .frame { position: absolute; left: 0; top: 0; width: 907px; height: 1200px; }
  .brand {
    position: absolute; left: 328px; top: 0; width: 250px; height: 200px;
    display: flex; align-items: center; justify-content: center; text-align: center;
    color: var(--white); font-family: "Oswald", sans-serif; font-weight: 500;
    font-size: 22px; line-height: 1.15; letter-spacing: 1px; text-transform: uppercase;
  }
  .headline { position: absolute; left: 0; width: 907px; text-align: center; }
  .headline-main { top: 200px; color: var(--red); font-size: 100px; line-height: 1; letter-spacing: 2px; }
  .headline-sub { top: 302px; color: var(--black); font-size: 54px; line-height: 1; letter-spacing: 1.5px; }
  .vehicles {
    position: absolute; left: 50px; top: 382px; width: 820px; height: 280px;
    background: linear-gradient(90deg, #d6d4d0 0%, #d6d4d0 22%, #1a1a1a 30%, #2a2a2a 62%, #3a62c9 70%, #2f58c4 100%);
    border-radius: 10px; opacity: .9;
  }
  .cash-text {
    position: absolute; left: 348px; top: 614px; width: 204px; text-align: center;
    color: var(--white); font-size: 45px; line-height: 50px;
  }
  .offer { position: absolute; left: 0; width: 907px; text-align: center; }
  .offer-list { top: 812px; color: var(--red); font-family: "Oswald", sans-serif; font-size: 27px; letter-spacing: .3px; }
  .offer-condition { top: 862px; color: var(--white); font-size: 30px; line-height: 42px; letter-spacing: .5px; }
  .offer-visit { top: 962px; color: var(--red); font-family: "Archivo", sans-serif; font-style: italic; font-weight: 800; font-size: 24px; letter-spacing: 1px; }
  .contact-band {
    position: absolute; left: 0; top: 1030px; width: 907px; height: 170px;
    background: linear-gradient(180deg, #161616 0%, #050505 100%);
    border-top: 1px solid #3a3a3a;
  }
  .phone {
    position: absolute; left: 0; top: 1040px; width: 907px; text-align: center;
    font-size: 60px; line-height: 76px; letter-spacing: 3px;
    color: var(--white);
    background: linear-gradient(180deg, #ffffff 0%, #ffffff 50%, #bdbdbd 100%);
    -webkit-background-clip: text; background-clip: text; -webkit-text-fill-color: transparent;
  }
  .coverage, .web {
    position: absolute; top: 1124px; color: var(--white);
    font-size: 17px; line-height: 26px; letter-spacing: .5px;
  }
  .coverage { left: 44px; font-size: 26px; line-height: 52px; letter-spacing: 2px; }
  .web { right: 44px; text-align: left; }
</style>
</head>
<body>
<main class="flyer">
  <div class="silver-field"></div>

  <div class="vehicles" role="img" aria-label="Photo of a white Vorano van, a black Ridgewalker 4WD and a blue truck side by side"></div>

  <svg class="frame" viewBox="0 0 907 1200" aria-hidden="true">
    <defs>
      <linearGradient id="chrome" x1="0" y1="0" x2="0" y2="1">
        <stop offset="0" stop-color="#ffffff"/>
        <stop offset=".5" stop-color="#9a9a9a"/>
        <stop offset="1" stop-color="#e6e6e6"/>
      </linearGradient>
      <radialGradient id="badge-red" cx=".4" cy=".35" r=".7">
        <stop offset="0" stop-color="#ff3a3a"/>
        <stop offset=".6" stop-color="#d3141c"/>
        <stop offset="1" stop-color="#7e070c"/>
      </radialGradient>
      <radialGradient id="badge-dark" cx=".5" cy=".4" r=".6">
        <stop offset="0" stop-color="#3a3a3a"/>
        <stop offset="1" stop-color="#0f0f0f"/>
      </radialGradient>
    </defs>
    <path d="M0 0 H907 V44 H640 L600 90 H307 L267 44 H0 Z" fill="#1a1a1a"/>
    <path d="M0 44 H267 L307 90 H600 L640 44 H907 V56 H646 L606 102 H301 L261 56 H0 Z" fill="url(#chrome)"/>
    <circle cx="453" cy="82" r="136" fill="url(#chrome)"/>
    <circle cx="453" cy="82" r="122" fill="url(#badge-dark)"/>
    <path d="M0 660 H300 L330 690 H577 L607 660 H907 V676 H614 L584 706 H323 L293 676 H0 Z" fill="url(#chrome)"/>
    <circle cx="450" cy="690" r="102" fill="url(#chrome)"/>
    <circle cx="450" cy="690" r="90" fill="url(#badge-red)"/>
  </svg>

  <div class="brand">Keystone<br>Vehicle Removal</div>

  <h1 class="headline headline-main">Wanted</h1>
  <h2 class="headline headline-sub">Dead or Alive</h2>

  <div class="cash-text">Get<br>Ca$h<br>Now</div>

  <p class="offer offer-list">WE BUY ONLY VANS, 4WDS, SUV, TRUCKS &amp; WE CAN COME TO YOU ANYWHERE</p>
  <p class="offer offer-condition">Damaged, Mechanical, Deregistered,<br>Crashed, No WOF - No Problem</p>
  <p class="offer offer-visit">*WE WILL COME TO YOU</p>

  <div class="contact-band"></div>
  <p class="phone">0800394826</p>
  <p class="coverage">NATION WIDE</p>
  <p class="web">info@keystoneremoval.co.nz<br>www.keystoneremoval.co.nz</p>
</main>
</body>
</html>
```